Orbel Appraisals website redesign

I would like to refresh my existing website of www.orbelappraisals-demo.com with new graphics, look and feel, as well as updated structure and wording. Content and layout changes have been uploaded to this project Brief.

My existing website has a dark feel. I am now looking for a light and energetic feel. Financial Services is my industry, so the website should be reflect that. I would also like to reflect the concepts of Trust, Service and Expertise.

The website must be serious and upmarket.

Target Market(s)

Corporate board members, CFO's, treasurers and controllers
Auditors, tax advisors, private equity and venture capital asset managers, investors, tax authorities

Industry/Entity Type

Financial Service

Coding

Coded - Design and coding required

Number of Pages Required

5+ page

Font styles to use
Sans Serif
Other font styles liked:
• Designer can choose another modern font

Colors
0355a3
3277b5
85acd3
eaf1f7
f37122
f68d4d
9bcb3c
acd037
cadf82

Requirements
Must have
• Good hi resolution pictures that convey "Finance", "Trust", "Service" or "Expertise".
• An anti-bot (such as Captcha) mechanism in the contact form.
Should not have
• Must not have all content on one rolling screen.

```html
<!DOCTYPE html>
<html lang="en">
<head>
<meta charset="utf-8">
<title>Orbel Appraisals – Home</title>
<link href="https://fonts.googleapis.com/css2?family=Lato:ital,wght@0,400;0,700;0,900;1,700&display=swap" rel="stylesheet">
<style>
:root{
  --blue:#0355a3;
  --blue-mid:#3277b5;
  --blue-soft:#85acd3;
  --blue-pale:#eaf1f7;
  --orange:#f37122;
  --orange-soft:#f68d4d;
  --green:#9bcb3c;
  --green-mid:#acd037;
  --green-soft:#cadf82;
  --ink:#1f2b3a;
  --text:#333;
  --footer-dark:#1b2533;
  --white:#fff;
}
*{margin:0;padding:0;box-sizing:border-box}
html,body{width:1200px;height:4132px;overflow:hidden;background:var(--white)}
body{position:relative;font-family:"Lato",sans-serif;color:var(--text)}
.abs{position:absolute}
a{color:inherit;text-decoration:none}

/* Header */
.brand{left:128px;top:78px;width:246px;height:42px;border:2px solid #777;display:flex;align-items:center;justify-content:center;font-size:20px;color:#666;letter-spacing:.5px;white-space:nowrap}
.topbar{left:530px;top:0;width:670px;height:64px}
.topbar-email{left:617px;top:20px;color:#fff;font-size:17px;display:flex;align-items:center;gap:12px;white-space:nowrap}
.topbar-call{left:919px;top:10px;color:#fff;white-space:nowrap}
.topbar-call small{display:block;font-size:11px;letter-spacing:.3px}
.topbar-call strong{display:block;font-size:22px;font-weight:700;margin-top:2px}
.nav{top:94px;left:0;font-size:17px;color:#222}
.nav a{position:absolute;white-space:nowrap}
.nav .active{color:var(--blue)}

/* Hero */
.hero{left:0;top:154px;width:1200px;height:640px}
.hero-title{left:117px;top:328px;color:#fff;font-size:41px;font-weight:700;white-space:nowrap}
.hero-text{left:122px;top:383px;color:#fff;font-size:17px;line-height:28.5px;width:430px}
.btn{display:flex;align-items:center;justify-content:center;background:var(--blue);color:#fff;border-radius:26px;font-size:17px}
.hero-btn{left:112px;top:492px;width:170px;height:50px}
.dot{width:12px;height:12px;border-radius:50%;background:var(--blue-soft);left:1104px}

/* Welcome */
.h2{width:1200px;left:0;text-align:center;font-weight:700;font-size:40px;letter-spacing:.3px}
.welcome-title{top:842px;color:var(--blue)}
.welcome-text{left:148px;width:904px;top:923px;text-align:center;font-size:14.5px;line-height:31px;color:#222}
.welcome-btn{left:515px;top:1155px;width:170px;height:51px}

/* Trust band */
.trust{left:0;top:1272px;width:1200px;height:480px;background:linear-gradient(180deg,var(--blue-mid),var(--blue))}
.trust-title{top:1376px;color:#fff}
.trust-text{left:178px;width:844px;top:1466px;text-align:center;color:#fff;font-size:14.5px;line-height:31px}
.ring{width:280px;height:280px;border-radius:50%;background:#fff;top:1629px}
.ring .photo{position:absolute;left:23px;top:23px;width:234px;height:234px;border-radius:50%}

/* Services */
.service-title{top:1998px;color:var(--ink)}
.service-text{left:232px;width:736px;top:2083px;text-align:center;font-size:14.5px;line-height:29px;color:#222}
.card{width:290px;height:195px;background:linear-gradient(180deg,var(--blue-mid) 0%,var(--blue) 100%);color:#fff;text-align:center;box-shadow:0 2px 4px rgba(0,0,0,.15)}
.card svg.icon{position:absolute;left:115px;top:16px}
.card .card-title{position:absolute;left:0;width:100%;top:100px;font-size:29px;white-space:nowrap}
.card .card-arrow{position:absolute;left:133px;top:152px}

/* How we work */
.how-panel{left:0;top:2788px;width:619px;height:406px;background:linear-gradient(180deg,var(--blue-mid),var(--blue))}
.how-title{left:0;width:584px;top:2906px;text-align:center;color:#fff;font-size:40px;font-weight:700}
.how-text{left:66px;width:454px;top:2979px;text-align:center;color:#fff;font-size:14px;line-height:28px}
.steps{left:584px;top:2887px;width:616px;height:409px;background:var(--blue-pale);box-shadow:-2px 3px 8px rgba(0,0,0,.25)}
.step-num{width:60px;height:60px;border-radius:50%;border:2px solid var(--green);color:var(--blue);font-size:32px;display:flex;align-items:center;justify-content:center;left:663px}
.step-text{left:743px;width:370px;font-size:18px;line-height:30px;color:#333}

/* Testimonials */
.says-title{top:3384px;color:var(--ink)}
.quote{background:#ececec;box-shadow:0 2px 6px rgba(0,0,0,.25);text-align:center;font-size:14px;line-height:25px;color:#333}
.quote p{position:absolute;left:24px;right:24px}
.quote .who{font-style:italic;font-weight:700;right:38px;left:auto}
.quote.featured{background:var(--blue);color:#fff}
.avatar{background:linear-gradient(160deg,#9fb0a0,#4d5a4e)}
.slide-btn{width:44px;height:44px;background:var(--orange);display:flex;align-items:center;justify-content:center}

/* Footer */
.footer-band{left:0;top:3909px;width:775px;height:109px;background:var(--blue)}
.footer-nav{top:3953px;color:#fff;font-size:15px}
.footer-nav a{position:absolute;white-space:nowrap}
.social{width:16px;height:16px;border-radius:50%;background:var(--green-mid);top:3955px}
.footer-bar{left:242px;top:4012px;width:958px;height:120px;background:var(--footer-dark);color:#fff}
.footer-contact{top:4047px;font-size:15px;display:flex;align-items:center;gap:14px;color:#fff;white-space:nowrap}
.footer-copy{left:296px;top:4099px;color:#fff;font-size:14px;white-space:nowrap}
</style>
</head>
<body>

<!-- Header -->
<div class="abs brand">ORBEL APPRAISALS</div>

<svg class="abs topbar" width="670" height="64" viewBox="0 0 670 64" aria-hidden="true">
  <polygon points="20,0 670,0 670,64 0,64" fill="#0355a3"/>
</svg>
<div class="abs topbar-email">
  <svg width="26" height="18" viewBox="0 0 26 18"><rect x="1" y="1" width="24" height="16" fill="none" stroke="#fff" stroke-width="2"/><polyline points="1,1 13,10 25,1" fill="none" stroke="#fff" stroke-width="2"/></svg>
  <span>info@orbelappraisals-demo.com</span>
</div>
<div class="abs topbar-call"><small>CALL US NOW</small><strong>070 555 0142</strong></div>

<nav class="abs nav">
  <a class="active" style="left:420px">Home</a>
  <a style="left:523px">Services</a>
  <a style="left:642px">News &amp; Views</a>
  <a style="left:805px">About</a>
  <a style="left:908px">Careers</a>
  <a style="left:1027px">Contact</a>
</nav>

<!-- Hero -->
<svg class="abs hero" width="1200" height="640" viewBox="0 0 1200 640">
  <defs>
    <linearGradient id="heroSky" x1="0" y1="0" x2="1" y2="1">
      <stop offset="0" stop-color="#06264f"/>
      <stop offset=".55" stop-color="#0a3f7c"/>
      <stop offset="1" stop-color="#3277b5"/>
    </linearGradient>
  </defs>
  <rect width="1200" height="640" fill="url(#heroSky)" role="img" aria-label="Night photograph of a lit waterfront hotel and conference building"/>
  <polygon points="0,640 1200,472 1200,640" fill="#fff"/>
  <polygon points="0,411 369,584 0,640" fill="#f37122"/>
</svg>
<h1 class="abs hero-title">Business &amp; Intellectual Property</h1>
<p class="abs hero-text">Lorem ipsum dolor sit amet, consectetur adipiscing elit, sed do eiusmod tempor incididunt ut labore et dolore magna aliqua.</p>
<a class="abs btn hero-btn">Get Started</a>
<span class="abs dot" style="top:390px"></span>
<span class="abs dot" style="top:409px"></span>
<span class="abs dot" style="top:429px;background:#fff"></span>

<!-- Welcome -->
<h2 class="abs h2 welcome-title">WELCOME TO&nbsp; ORBEL APPRAISALS</h2>
<p class="abs welcome-text">Orbel Appraisals, founded in 2012, is a boutique valuation advisory practice servicing companies throughout Europe and North America. We have offices in Leiden and Amsterdam. Through our affiliate partners, we also have offices in New York and London offering transfer pricing, derivatives modelling, and machinery &amp; equipment valuation. Our clients come from a broad range of industries with valuations ranging between micro-cap and large-cap. Orbel Appraisals assists companies with valuations of businesses, financial instruments, derivatives, personal property and intellectual property (such as brand assets and patents) for transaction, fiscal, legal and accounting purposes, particularly in cross-border situations.</p>
<a class="abs btn welcome-btn">Read More</a>

<!-- Trust -->
<div class="abs trust" role="img" aria-label="Faint blue-tinted city skyline"></div>
<h2 class="abs h2 trust-title">TRUST, SERVICE &amp; EXPERTISE</h2>
<p class="abs trust-text">Trust is paramount. Clients rely on Orbel Appraisals for confidentiality, transparency and independence. Service is front and center in Orbel Appraisals' product offerings. Orbel Appraisals considers the needs of all stakeholders and the personal needs of the client team involved. Orbel Appraisals offers more than a decade of valuation experience and maintains its commitment to continual professional development.</p>
<div class="abs ring" style="left:129px"><div class="photo" role="img" aria-label="Modern apartment building against a blue sky" style="background:linear-gradient(160deg,#4f8fd0,#8a6a4e 70%,#3a2c20)"></div></div>
<div class="abs ring" style="left:460px"><div class="photo" role="img" aria-label="Glass office tower in grey daylight" style="background:linear-gradient(170deg,#9fb0c4,#3e4a58 60%,#1c242e)"></div></div>
<div class="abs ring" style="left:774px"><div class="photo" role="img" aria-label="Glass-fronted office building under a clear sky" style="background:linear-gradient(160deg,#5b9be0,#b7c9da 55%,#6c747c)"></div></div>

<!-- Services -->
<h2 class="abs h2 service-title">OUR SERVICE</h2>
<p class="abs service-text">Transactions can take many forms. You could be either the buyer or seller transacting in a whole company or only a part, as an individual investor or part of a group. Payment can be in cash or in kind, and can be paid at transaction date or in the future. Transactions may involve ordinary shares, preference shares, debt, convertibles, warrants, options, amongst others. There are many types of transactions and they can be complex.</p>

<div class="abs card" style="left:125px;top:2254px">
  <svg class="icon" width="60" height="60" viewBox="0 0 60 60" fill="none" stroke="#fff" stroke-width="2"><rect x="8" y="20" width="44" height="30"/><rect x="18" y="6" width="20" height="24"/><line x1="14" y1="36" x2="46" y2="36"/><line x1="14" y1="43" x2="46" y2="43"/></svg>
  <div class="card-title">Transaction Support</div>
  <svg class="card-arrow" width="24" height="16" viewBox="0 0 24 16" fill="none" stroke="#fff" stroke-width="2"><line x1="1" y1="8" x2="22" y2="8"/><polyline points="15,1 22,8 15,15"/></svg>
</div>
<div class="abs card" style="left:455px;top:2254px">
  <svg class="icon" width="60" height="60" viewBox="0 0 60 60" fill="none" stroke="#fff" stroke-width="2"><rect x="18" y="8" width="24" height="22"/><path d="M6 40 Q20 32 30 38 L44 38 Q50 38 50 44 L30 46"/><path d="M6 50 L40 52 L56 40"/></svg>
  <div class="card-title">Financial Reporting</div>
  <svg class="card-arrow" width="24" height="16" viewBox="0 0 24 16" fill="none" stroke="#fff" stroke-width="2"><line x1="1" y1="8" x2="22" y2="8"/><polyline points="15,1 22,8 15,15"/></svg>
</div>
<div class="abs card" style="left:784px;top:2254px">
  <svg class="icon" width="60" height="60" viewBox="0 0 60 60" fill="none" stroke="#fff" stroke-width="2"><polygon points="30,6 52,20 8,20"/><rect x="10" y="20" width="40" height="30"/><line x1="18" y1="28" x2="18" y2="44"/><line x1="30" y1="28" x2="30" y2="44"/><line x1="42" y1="28" x2="42" y2="44"/><line x1="6" y1="52" x2="54" y2="52"/></svg>
  <div class="card-title">Fiscal Valuations</div>
  <svg class="card-arrow" width="24" height="16" viewBox="0 0 24 16" fill="none" stroke="#fff" stroke-width="2"><line x1="1" y1="8" x2="22" y2="8"/><polyline points="15,1 22,8 15,15"/></svg>
</div>
<div class="abs card" style="left:125px;top:2493px">
  <svg class="icon" width="60" height="60" viewBox="0 0 60 60" fill="none" stroke="#fff" stroke-width="2"><rect x="22" y="6" width="32" height="20"/><circle cx="12" cy="18" r="5"/><circle cx="12" cy="40" r="4"/><circle cx="24" cy="40" r="4"/><circle cx="36" cy="40" r="4"/><circle cx="48" cy="40" r="4"/><line x1="6" y1="52" x2="54" y2="52"/></svg>
  <div class="card-title">Finance Training</div>
  <svg class="card-arrow" width="24" height="16" viewBox="0 0 24 16" fill="none" stroke="#fff" stroke-width="2"><line x1="1" y1="8" x2="22" y2="8"/><polyline points="15,1 22,8 15,15"/></svg>
</div>
<div class="abs card" style="left:455px;top:2493px">
  <svg class="icon" width="60" height="60" viewBox="0 0 60 60" fill="none" stroke="#fff" stroke-width="2"><rect x="24" y="6" width="14" height="24" transform="rotate(-45 31 18)"/><line x1="26" y1="26" x2="8" y2="44"/><rect x="28" y="46" width="26" height="8"/></svg>
  <div class="card-title">Legal Support</div>
  <svg class="card-arrow" width="24" height="16" viewBox="0 0 24 16" fill="none" stroke="#fff" stroke-width="2"><line x1="1" y1="8" x2="22" y2="8"/><polyline points="15,1 22,8 15,15"/></svg>
</div>
<div class="abs card" style="left:784px;top:2493px">
  <svg class="icon" width="60" height="60" viewBox="0 0 60 60" fill="none" stroke="#fff" stroke-width="2"><line x1="30" y1="4" x2="30" y2="12"/><rect x="22" y="12" width="16" height="10"/><polygon points="30,16 50,28 10,28"/><rect x="12" y="28" width="36" height="22"/><line x1="20" y1="32" x2="20" y2="48"/><line x1="30" y1="32" x2="30" y2="48"/><line x1="40" y1="32" x2="40" y2="48"/><line x1="6" y1="54" x2="54" y2="54"/></svg>
  <div class="card-title">Capital Advisory</div>
  <svg class="card-arrow" width="24" height="16" viewBox="0 0 24 16" fill="none" stroke="#fff" stroke-width="2"><line x1="1" y1="8" x2="22" y2="8"/><polyline points="15,1 22,8 15,15"/></svg>
</div>

<!-- How we work -->
<div class="abs how-panel" role="img" aria-label="Blue-tinted city skyline"></div>
<h2 class="abs how-title">HOW WE WORK?</h2>
<p class="abs how-text">Lorem ipsum dolor sit amet, consectetur adipiscing elit, sed do eiusmod tempor incididunt ut labore et dolore magna aliqua. Quis ipsum suspendisse ultrices gravida</p>
<div class="abs steps"></div>
<div class="abs step-num" style="top:2929px">1</div>
<p class="abs step-text" style="top:2929px">Lorem ipsum dolor sit amet, consectetur adipiscing elit, sed do eiusmod tempor</p>
<div class="abs step-num" style="top:3010px">2</div>
<p class="abs step-text" style="top:3010px">Neque porro quisquam est qui dolorem ipsum quia dolor sit amet,</p>
<div class="abs step-num" style="top:3095px">3</div>
<p class="abs step-text" style="top:3092px">It is a long established fact that a reader will be distracted by the readable content</p>
<div class="abs step-num" style="top:3188px">4</div>
<p class="abs step-text" style="top:3183px">There are many variations of passages of Lorem Ipsum available, but the majority</p>

<!-- Testimonials -->
<h2 class="abs h2 says-title">WHAT PEOPLE SAY ABOUT US</h2>
<a class="abs slide-btn" style="left:40px;top:3617px"><svg width="26" height="20" viewBox="0 0 26 20" fill="none" stroke="#fff" stroke-width="2"><line x1="25" y1="10" x2="2" y2="10"/><polyline points="10,2 2,10 10,18"/></svg></a>
<a class="abs slide-btn" style="left:1118px;top:3617px"><svg width="26" height="20" viewBox="0 0 26 20" fill="none" stroke="#fff" stroke-width="2"><line x1="1" y1="10" x2="24" y2="10"/><polyline points="16,2 24,10 16,18"/></svg></a>

<div class="abs quote" style="left:119px;top:3540px;width:284px;height:189px">
  <p style="top:62px">Lorem ipsum dolor sit amet, consectetur adipiscing elit, sed do eiusmod tempor incididunt ut</p>
  <p class="who" style="top:142px">-Lorem ipsum dolor</p>
</div>
<div class="abs avatar" style="left:234px;top:3515px;width:55px;height:55px" role="img" aria-label="Client portrait"></div>

<div class="abs quote featured" style="left:440px;top:3527px;width:320px;height:214px">
  <p style="top:76px">Julian is a corporate finance advisor with extensive and wide-ranging knowledge and experience in the area.</p>
  <p class="who" style="top:156px">-Mara Lindqvist,</p>
</div>
<div class="abs avatar" style="left:570px;top:3497px;width:61px;height:61px" role="img" aria-label="Client portrait"></div>

<div class="abs quote" style="left:796px;top:3540px;width:284px;height:189px">
  <p style="top:62px">Lorem ipsum dolor sit amet, consectetur adipiscing elit, sed do eiusmod tempor incididunt ut</p>
  <p class="who" style="top:142px">-Lorem ipsum dolor</p>
</div>
<div class="abs avatar" style="left:911px;top:3515px;width:55px;height:55px" role="img" aria-label="Client portrait"></div>

<!-- Footer -->
<div class="abs" style="left:200px;top:3833px;width:180px;height:76px;background:linear-gradient(180deg,#fff,#e2e6ec)" role="img" aria-label="Faint grey city skyline illustration"></div>
<div class="abs" style="left:818px;top:3850px;width:382px;height:162px;background:linear-gradient(180deg,#fff 0%,#f68d4d 45%,#1b3a66 100%)" role="img" aria-label="Colourful city skyline illustration"></div>
<div class="abs" style="left:0;top:4018px;width:242px;height:114px;background:linear-gradient(180deg,#eaf1f7,#b9c4d0)" role="img" aria-label="Grey building pattern illustration"></div>

<div class="abs footer-band"></div>
<nav class="abs footer-nav" style="left:0">
  <a style="left:107px">Home</a>
  <a style="left:177px">Services</a>
  <a style="left:260px">News &amp; Views</a>
  <a style="left:378px">About</a>
  <a style="left:448px">Careers</a>
  <a style="left:530px">Contact</a>
</nav>
<span class="abs social" style="left:618px"></span>
<span class="abs social" style="left:651px"></span>
<span class="abs social" style="left:688px"></span>
<span class="abs social" style="left:725px"></span>

<div class="abs footer-bar"></div>
<div class="abs footer-contact" style="left:290px">
  <svg width="20" height="20" viewBox="0 0 20 20"><path d="M4 1 L8 5 L6 8 Q8 12 12 14 L15 12 L19 16 L16 19 Q8 19 1 4 Z" fill="#fff"/></svg>
  <span>+31 70 555 0142</span>
</div>
<div class="abs footer-contact" style="left:487px">
  <svg width="26" height="18" viewBox="0 0 26 18"><rect x="1" y="1" width="24" height="16" fill="none" stroke="#fff" stroke-width="2"/><polyline points="1,1 13,10 25,1" fill="none" stroke="#fff" stroke-width="2"/></svg>
  <span>info@orbelappraisals-demo.com</span>
</div>
<div class="abs footer-contact" style="left:740px;font-size:12.5px">
  <svg width="14" height="20" viewBox="0 0 14 20"><path d="M7 0 C3 0 0 3 0 7 C0 12 7 20 7 20 C7 20 14 12 14 7 C14 3 11 0 7 0 Z" fill="#fff"/><circle cx="7" cy="7" r="2.5" fill="#1b2533"/></svg>
  <span>Kadeweg 14, 2300 AB Leiden The Netherlands</span>
</div>
<p class="abs footer-copy">© 2019 Copyrights Company Name | All Rights Reserved</p>

</body>
</html>
```